New homepage design www.marblequill.nl

We need a new website design to go with our new designed logo.
We are a relativly small basketballclub that would like a shiny new webdesign for our homepage. We want te be able to create a real homepage/base for our clubmembers, where they can find news, upcoming events (agenda/calendar) and the related info on playing basketball at our club (games/tasks/teams and all).

The current website is located at: www.marblequill.nl but is an outdated and not so appealing design.
There are no real designfeatures of the current site that have to be transferred to the new site.
Coding in HTML/CSS/JS/JPEG/PNG is enough, making a dynamic website will be my task. I just need the design in HTML (preferrably HTML 5)

There is not a huge budget, we are a club without a main sponsor.

Feel free to be creative and amaze us!

Text for the page in the new design will be created by us, you may use some sample text for filling.

Currently used pictures in the site don't have to be transferred to the new page (preferrably not!)

Reason: For Newyear/holiday reasons

Tomorrow we will pick a design.

• The new logo as uploaded and attached.
News page.
Agenda page
HTML compatible same look and feel in all modern browsers (IE, FireFox, Chrome, Safari)
• HTML 5 validated and approved

```html
<!DOCTYPE html>
<html lang="en">
<head>
<meta charset="utf-8">
<title>Marblequill Basketball Club</title>
<link rel="stylesheet" href="https://fonts.googleapis.com/css2?family=Lilita+One&family=Arimo:wght@400;700&family=Open+Sans:wght@700&display=swap">
<style>
:root{
  --night:#1a181e;
  --night-deep:#0f0e12;
  --footer:#151515;
  --ink:#111;
  --text:#333;
  --muted:#666;
  --lilac:#b49ae0;
  --purple:#7b3fc2;
  --purple-dark:#5a2a96;
  --band:#ebebeb;
  --orange:#e2651c;
  --yellow:#f5d800;
  --white:#fff;
  --link:#5a2a96;
}
*{margin:0;padding:0;box-sizing:border-box}
html,body{width:1133px;height:1200px;overflow:hidden}
body{position:relative;background:var(--band);font-family:"Arimo",Arial,sans-serif;color:var(--text)}
.heading{font-family:"Lilita One",Impact,sans-serif;font-weight:400;letter-spacing:.5px;text-transform:uppercase}
a{color:inherit}

/* hero */
.hero{position:absolute;left:0;top:0;width:1133px;height:397px;
  background:radial-gradient(ellipse 520px 260px at 720px 260px,#3a2f4e 0%,#221d2a 55%,var(--night-deep) 100%);}
.brand{position:absolute;left:168px;top:70px;display:flex;align-items:center;gap:10px}
.brand-dot{width:34px;height:34px;border-radius:50%;background:var(--orange)}
.brand-name{font-family:"Lilita One",Impact,sans-serif;font-size:34px;color:var(--white);letter-spacing:1px}
.hero-photo{position:absolute;left:133px;top:195px;width:310px;height:202px;
  background:linear-gradient(160deg,#d9d9d9 0%,#8d8d8d 45%,#b8542a 75%,#3a2a24 100%);border-radius:14px 14px 0 0}
.utility{position:absolute;right:140px;top:52px;display:flex;align-items:baseline;gap:10px;color:var(--white)}
.utility a{font-size:11px}
.utility .phone{font-family:"Arimo",sans-serif;font-weight:700;font-size:17px;margin-left:16px}
.nav{position:absolute;left:433px;top:83px;display:flex;gap:18px}
.nav a{display:block;height:28px;line-height:29px;padding:0 14px;background:#000;border-radius:6px;color:var(--white);
  font-family:"Lilita One",Impact,sans-serif;font-size:15px;text-decoration:none;letter-spacing:.5px}
.hero-copy{position:absolute;left:592px;top:163px;width:410px}
.hero-copy h1{font-size:29px;line-height:32px;color:var(--white)}
.hero-copy p{margin-top:20px;font-size:18px;line-height:21px;color:var(--lilac)}
.btn-more{position:absolute;left:592px;top:327px;width:135px;height:28px;border-radius:6px;
  background:linear-gradient(#fafafa,#c9c9c9);color:var(--ink);font-family:"Lilita One",sans-serif;font-size:14px;
  display:flex;align-items:center;padding-left:10px;gap:22px;text-decoration:none}
.btn-more svg{width:7px;height:7px}
.slider-arrows{position:absolute;left:925px;top:374px;width:68px;height:23px;border-radius:6px 6px 0 0;
  background:linear-gradient(#e4e4e4,#bdbdbd);display:flex;justify-content:space-around;align-items:center}
.slider-arrows svg{width:6px;height:6px}
.hero-edge{position:absolute;left:0;top:397px;width:1133px;height:6px;background:linear-gradient(#cfcfcf,var(--band))}

/* content */
.column{position:absolute;top:427px}
.column h2{font-size:17px;color:var(--ink)}
.join{left:137px;width:265px}
.join-item{display:flex;gap:14px;margin-top:17px;height:87px}
.join-item + .join-item{border-top:1px solid #d6d6d6;padding-top:10px;height:104px;margin-top:10px}
.thumb{flex:0 0 70px;height:90px;border-radius:2px}
.join-item h3{font-weight:400;font-size:14px;color:var(--ink);margin-bottom:8px}
.join-item p{font-size:11px;line-height:17px;color:var(--muted)}

.dates{left:431px;width:270px}
.date-list{list-style:none;margin-top:17px}
.date-list li{display:flex;gap:13px;height:62.5px}
.cal{width:44px;height:44px;border-radius:8px;background:#555;border:2px solid #555;display:flex;flex-direction:column;overflow:hidden}
.cal .month{flex:0 0 28px;background:var(--white);border-radius:6px 6px 0 0;font-weight:700;font-size:13px;color:var(--ink);text-align:center;line-height:28px}
.cal .day{color:var(--white);font-size:9px;text-align:center;line-height:12px;font-weight:700}
.cal.match{background:#222;border-color:#222}
.cal.match .month{background:var(--yellow)}
.date-list h3{font-weight:400;font-size:14px;color:var(--ink);margin-top:3px}
.date-list p{font-size:11px;color:var(--muted);margin-top:6px}
.dates .all-link{display:block;font-size:11px;color:var(--link);margin-top:-4px}

.scorers{position:absolute;left:727px;top:428px;width:266px;height:312px;background:var(--white);border:4px solid #d8d8d8}
.scorers-head{height:30px;background:linear-gradient(var(--purple),var(--purple-dark));display:flex;align-items:center;justify-content:space-between;padding:0 9px}
.scorers-head h2{font-size:14px;color:var(--white)}
.scorers-head span{display:flex;gap:7px}
.scorers-head svg{width:6px;height:6px}
.scorers table{width:100%;border-collapse:collapse;font-size:11px;color:var(--ink)}
.scorers td{height:24px;padding:0 10px}
.scorers td:last-child{text-align:right}
.scorers tr:nth-child(even) td{background:#f0f0f0}
.roster-btn{display:block;margin:6px 4px 0;height:22px;background:linear-gradient(#e6e6e6,#c4c4c4);text-align:center;line-height:23px;
  font-family:"Lilita One",sans-serif;font-size:13px;color:#333;text-decoration:none}

/* sponsors */
.sponsors{position:absolute;left:0;top:820px;width:1133px;height:105px;background:linear-gradient(#fdfdfd,#e6e6e6);
  border-top:1px solid #d0d0d0;display:flex;padding-left:117px}
.sponsor{width:210px;height:70px;margin-top:15px;display:flex;align-items:center;justify-content:center;
  font-family:"Open Sans",sans-serif;font-weight:700;font-size:31px;color:#a9a9a9;background:rgba(255,255,255,.6);border-right:1px solid #d5d5d5;margin-right:15px}
.sponsor:last-child{border-right:0}

/* footer */
.footer{position:absolute;left:0;top:925px;width:1133px;height:275px;background:var(--footer);color:var(--white)}
.footer h2{font-size:17px;color:var(--white);position:absolute;top:23px}
.fcol{position:absolute;top:0}
.links{left:137px}
.links ul{list-style:none;position:absolute;top:67px;width:200px}
.links li{display:flex;align-items:center;gap:12px;height:22.3px;font-size:10.5px}
.links li::before{content:"";width:12px;height:12px;border-radius:50%;background:radial-gradient(circle at 35% 35%,#f08a45,var(--orange) 60%,#a8430e)}
.locate{left:357px}
.map{position:absolute;top:69px;width:194px;height:142px;background:linear-gradient(135deg,#e9e6df 0%,#dcd9cf 50%,#c9d6e4 100%);border:1px solid #555}
.about{left:577px}
.about p{position:absolute;top:68px;width:200px;font-size:10px;line-height:17.5px;color:#ddd}
.contact{left:797px}
.contact ul{list-style:none;position:absolute;top:66px;width:200px}
.contact li{display:flex;align-items:center;gap:12px;height:22.3px;font-size:10.5px}
.contact svg{width:13px;height:11px;flex:0 0 13px}
.back-top{position:absolute;right:140px;top:251px;font-size:10.5px}
</style>
</head>
<body>

<header class="hero">
  <div class="brand"><span class="brand-dot"></span><span class="brand-name">MARBLEQUILL</span></div>
  <div class="hero-photo" role="img" aria-label="Photo of a basketball dropping through the hoop and net"></div>

  <div class="utility">
    <a href="#">About Us</a><a href="#">Contact Us</a><span class="phone">07700 900 412</span>
  </div>
  <nav class="nav">
    <a href="#">TEAM NEWS</a><a href="#">SCHEDULE/RESULTS</a><a href="#">TEAM HISTORY</a><a href="#">CLUB MEMBERS</a>
  </nav>

  <div class="hero-copy">
    <h1 class="heading">New Member Trial<br>Sessions</h1>
    <p>Think you have what it takes to make the team? Come down and find out. Play some basketball and have fun.</p>
  </div>
  <a class="btn-more" href="#"><svg viewBox="0 0 8 8"><path d="M1 0l6 4-6 4z" fill="#222"/></svg>READ MORE</a>
  <div class="slider-arrows">
    <svg viewBox="0 0 8 8"><path d="M7 0L1 4l6 4z" fill="#333"/></svg>
    <svg viewBox="0 0 8 8"><path d="M1 0l6 4-6 4z" fill="#333"/></svg>
  </div>
</header>
<div class="hero-edge"></div>

<section class="column join">
  <h2 class="heading">Why You Should Join Us</h2>
  <div class="join-item">
    <div class="thumb" role="img" aria-label="Photo of a player drinking water" style="background:linear-gradient(#6d8fb0,#b5462c)"></div>
    <div><h3>Get In Shape</h3><p>Quisque auctor neque a nisl sollicitudin posuere. Aliquam in enim vitae turpis euismod cursus. Aenean libero ante</p></div>
  </div>
  <div class="join-item">
    <div class="thumb" role="img" aria-label="Photo of a player lifting a trophy" style="background:linear-gradient(#2a2a34,#6a5f7a)"></div>
    <div><h3>Compete</h3><p>Quisque auctor neque a nisl sollicitudin posuere. Aliquam in enim vitae turpis euismod cursus. Aenean libero ante</p></div>
  </div>
  <div class="join-item">
    <div class="thumb" role="img" aria-label="Photo of teammates sitting together" style="background:linear-gradient(#c8b59a,#6d7a5a)"></div>
    <div><h3>Make Friends</h3><p>Quisque auctor neque a nisl sollicitudin posuere. Aliquam in enim vitae turpis euismod cursus. Aenean libero ante</p></div>
  </div>
</section>

<section class="column dates">
  <h2 class="heading">Upcoming Important Dates</h2>
  <ul class="date-list">
    <li><div class="cal"><span class="month">Dec</span><span class="day">6</span></div><div><h3>Team Training</h3><p>8:00-9:00 Main Gym</p></div></li>
    <li><div class="cal"><span class="month">Dec</span><span class="day">6</span></div><div><h3>Team Training</h3><p>8:00-9:00 Main Gym</p></div></li>
    <li><div class="cal"><span class="month">Aug</span><span class="day">9</span></div><div><h3>Team Training</h3><p>8:00-9:00 Main Gym</p></div></li>
    <li><div class="cal match"><span class="month">Jun</span><span class="day">14</span></div><div><h3>League Match</h3><p>4:00-6:00 Main Gym</p></div></li>
    <li><div class="cal"><span class="month">Mar</span><span class="day">24</span></div><div><h3>Team Training</h3><p>8:00-9:00 Main Gym</p></div></li>
  </ul>
  <a class="all-link" href="#">View Full Schedule Of Events</a>
</section>

<aside class="scorers">
  <div class="scorers-head">
    <h2 class="heading">Top Scorers 2011/2012</h2>
    <span><svg viewBox="0 0 8 8"><path d="M7 0L1 4l6 4z" fill="#fff"/></svg><svg viewBox="0 0 8 8"><path d="M1 0l6 4-6 4z" fill="#fff"/></svg></span>
  </div>
  <table>
    <tr><td>Bram Dekker</td><td>25.6ppg</td></tr>
    <tr><td>Milo Verhoef</td><td>22.4ppg</td></tr>
    <tr><td>Madeup Name</td><td>16.8ppg</td></tr>
    <tr><td>Tomas Moerland</td><td>15.4ppg</td></tr>
    <tr><td>Mats Kuiper</td><td>14.7ppg</td></tr>
    <tr><td>Gijs Molenaar</td><td>11.0ppg</td></tr>
    <tr><td>Daan Fokker</td><td>7.6ppg</td></tr>
    <tr><td>Bas Janssen</td><td>5.4ppg</td></tr>
    <tr><td>Mick Jorissen</td><td>3.2ppg</td></tr>
    <tr><td>Ruud Ubbink</td><td>2.9ppg</td></tr>
  </table>
  <a class="roster-btn" href="#">VIEW FULL ROSTER STATS</a>
</aside>

<section class="sponsors">
  <div class="sponsor">SPONSOR1</div>
  <div class="sponsor">SPONSOR2</div>
  <div class="sponsor">SPONSOR3</div>
  <div class="sponsor">SPONSOR4</div>
</section>

<footer class="footer">
  <div class="fcol links">
    <h2 class="heading">Important Links</h2>
    <ul>
      <li><a href="#">League Website</a></li>
      <li><a href="#">Basketball Rules &amp; History</a></li>
      <li><a href="#">Affiliate Website</a></li>
      <li><a href="#">Training Methods &amp; Techniques</a></li>
      <li><a href="#">League Table</a></li>
      <li><a href="#">Other Websites</a></li>
    </ul>
  </div>
  <div class="fcol locate">
    <h2 class="heading">Locate Us</h2>
    <div class="map" role="img" aria-label="Street map showing the club location"></div>
  </div>
  <div class="fcol about">
    <h2 class="heading">About Us</h2>
    <p>molestie at nulla. Donec commodo lacus non dui egestas non bibendum tellus cursus. Suspendisse sit amet est odio. Suspendisse semper, turpis eget feugiat venenatis.tortor eu libero euismod vel congue ligula ullamcorper</p>
  </div>
  <div class="fcol contact">
    <h2 class="heading">Contact Details</h2>
    <ul>
      <li><svg viewBox="0 0 13 11"><rect x="1" y="1" width="11" height="9" rx="1" fill="#bbb"/><rect x="3" y="3" width="7" height="2" fill="#555"/></svg>07700 900 412</li>
      <li><svg viewBox="0 0 13 11"><rect x=".5" y="1.5" width="12" height="8" fill="#eee"/><path d="M.5 1.5l6 4.5 6-4.5" fill="none" stroke="#777"/></svg><a href="#">info@marblequill.nl</a></li>
      <li><svg viewBox="0 0 13 11"><rect x="1" y="0" width="11" height="11" rx="2" fill="#4a68a8"/></svg><a href="#">Marblequill Social</a></li>
      <li><svg viewBox="0 0 13 11"><rect x="1" y="0" width="11" height="11" rx="2" fill="#c8342c"/></svg><a href="#">Marblequill Video</a></li>
      <li><svg viewBox="0 0 13 11"><rect x="1" y="0" width="11" height="11" fill="#d9e6f2"/><path d="M3 3h7M3 5.5h7M3 8h5" stroke="#4a7ab0"/></svg><a href="#">Contact Form</a></li>
    </ul>
  </div>
  <a class="back-top" href="#">Back To Top</a>
</footer>

</body>
</html>
```